シニア向け新商品(飲料)のLP制作をお願いします。

■制作数: 1ページ
■素材: 商品写真、文言はこちらで用意させていただきます。
■コーディング: 不要
■デザイン:PC版
■納品ファイル :イラストレーター形式 (.ai)
※完成後は当方でスマホ化を行うため、アウトラインなしもお願いします
■合計費用:5万円

※今回のデザインですが、別途添付しておりますラフ画(PowerPoint or PDF)の部分までお願いします。そのデザインにて恐縮ですが、選考をさせていただき、決定者様に3万円、また、ページの続き(下部の管理体制や価格についてのページデザインフィニッシュまで)は、同じ選考者様に+2万円にてお願いできればありがたく存じます。(選考決定の方への報酬は合計5万円になります。)

※パッケージ素材について
(PDF以外をご希望の場合は、相談して進めさせていただければと思います。 )

※テキストやキャッチコピーについては、そのままでもかまいませんし、
デザイン上、魅力的なものへリライト希望でしたら、添削等、自由とさせていただきます。

何卒よろしくお願い申し上げます。
ファイル添付が見られないというご指摘を受けたので、ファイルえを追加させていただきます。お手数ですがご参考いただければと存じます。
依頼金額を36000円に変更して、延長しました。
今回LP制作依頼が初めてであり、比較検討したく、もう少し様々なパターンな提案が欲しく延長させていただきました。
シニア層向けの若々しさが伝わるシンプルなデザインを希望します。
ラフ画像の指示が細かくて制作しにくい場合は多少削ってしまって全然問題ございませんので、ご検討していただければと思います。
また、不明点等がございましたら細かいことでもお申し付けください。
何卒よろしくお願いします。
期間を延長させていただきます。
皆様のご応募お待ちしております。

デザインがシンプルで今回のターゲット層にマッチしていたため。
また、修正や指摘に対しても柔軟かつ迅速に対応してくれて、制作をスピーディに進めていただいたことも大きかったです。

皆さま、この度はご提案ありがとうございます。
落選させていただい方につきましても、大変申し訳ございません。
またこのような機会を設けさせていただきたいので、その際は是非ともよろしくお願いいたします。

```html
<!DOCTYPE html>
<html lang="ja">
<head>
<meta charset="utf-8">
<title>あゆみ麦茶 | 理想的な水分補給を応援</title>
<link href="https://fonts.googleapis.com/css2?family=Noto+Sans+JP:wght@400;500;700;900&family=Noto+Serif+JP:wght@600;700;900&display=swap" rel="stylesheet">
<style>
:root{
  --brown:#5b3a1d;
  --brown-dark:#3e2612;
  --brown-soft:#8a6440;
  --gold:#c59a3a;
  --cream:#fbf6ea;
  --beige:#f1e6cf;
  --green:#4c8c2c;
  --green-light:#8cc152;
  --orange:#ec7a1c;
  --red:#d6392b;
  --text:#3b2c1f;
  --sky:#cfe6f4;
  --wood:#c9a36b;
  --white:#fff;
}
*{box-sizing:border-box;margin:0;padding:0}
html,body{width:1200px;height:4976px;overflow:hidden}
body{font-family:"Noto Sans JP",sans-serif;color:var(--text);background:var(--white);line-height:1.6}
.serif{font-family:"Noto Serif JP",serif}
.ph{display:block}

/* header */
.site-header{height:56px;background:var(--white);border-bottom:3px solid var(--gold);display:flex;align-items:center;justify-content:space-between;padding:0 40px}
.brand{display:flex;align-items:center;gap:10px;font-weight:700;font-size:24px;color:var(--brown)}
.brand-dot{width:18px;height:18px;border-radius:50%;background:var(--gold)}
.tel{display:flex;align-items:center;gap:12px}
.tel-tag{font-size:13px;border:1px solid var(--brown);padding:2px 8px;color:var(--brown)}
.tel-num{font-size:30px;font-weight:900;color:var(--brown);display:flex;align-items:center;gap:6px}

/* hero */
.hero{position:relative;height:756px;overflow:hidden}
.hero-bg{position:absolute;inset:0;background:linear-gradient(180deg,#e9f3d6 0%,#c8dfa4 55%,#a5c77a 100%)}
.hero-people{position:absolute;right:60px;top:190px;width:560px;height:540px;border-radius:20px;background:linear-gradient(160deg,#f3efe2,#dbe8c6)}
.hero-copy{position:absolute;right:60px;top:40px;width:720px;text-align:center}
.hero-copy .sub{font-size:44px;font-weight:900;color:var(--brown-dark)}
.hero-copy .main{font-size:56px;font-weight:900;color:var(--brown-dark);line-height:1.2}
.hero-copy .main em{font-style:normal;color:var(--green)}
.pack{position:absolute;left:70px;top:140px;width:380px;height:420px;border-radius:10px;background:linear-gradient(160deg,#c58a4a,#7b4a22)}
.pack-spec{position:absolute;left:70px;top:580px;width:380px;text-align:center;font-size:20px;font-weight:700;color:var(--brown-dark)}
.pack-note{position:absolute;left:70px;top:620px;width:380px;text-align:center;font-size:16px;color:var(--brown-dark)}
.badge{position:absolute;border-radius:50%;display:flex;flex-direction:column;align-items:center;justify-content:center;text-align:center;color:var(--white);font-weight:900;line-height:1.2;white-space:nowrap}
.badge-hot{left:30px;top:70px;width:110px;height:110px;background:var(--red);font-size:22px}
.badge-ice{left:150px;top:60px;width:100px;height:100px;background:#3b8fd0;font-size:20px}
.badge-price{right:40px;top:500px;width:170px;height:170px;background:var(--green);font-size:18px}
.badge-price b{font-size:44px;display:block;line-height:1.1}
.award{position:absolute;left:480px;top:640px;background:rgba(255,255,255,.9);padding:8px 18px;border-radius:6px;font-size:17px;font-weight:700;color:var(--brown)}
.feature-tags{position:absolute;left:470px;top:190px;display:flex;flex-direction:column;gap:14px}
.feature-tags span{width:110px;height:110px;border-radius:50%;background:rgba(255,255,255,.92);border:3px solid var(--gold);display:flex;align-items:center;justify-content:center;text-align:center;font-size:18px;font-weight:700;color:var(--brown);line-height:1.3}

.guarantee{height:76px;background:var(--green);color:var(--white);display:flex;align-items:center;justify-content:center;font-size:34px;font-weight:900;letter-spacing:.04em}
.guarantee em{font-style:normal;color:#ffe45c}

/* sample */
.sample{height:160px;background:var(--cream);padding-top:14px}
.sample-head{margin:0 auto;width:760px;background:var(--orange);color:var(--white);text-align:center;font-size:30px;font-weight:900;border-radius:6px;padding:4px 0}
.sample-head em{font-style:normal;color:#fff36a}
.sample-row{display:flex;justify-content:center;gap:24px;margin-top:16px}
.sample-offer{width:420px;height:80px;border:3px solid var(--red);background:var(--white);color:var(--red);font-size:24px;font-weight:900;display:flex;align-items:center;justify-content:center;text-align:center;line-height:1.25}
.btn{width:260px;height:80px;border-radius:10px;color:var(--white);font-size:24px;font-weight:900;display:flex;align-items:center;justify-content:center;gap:10px;box-shadow:0 4px 0 rgba(0,0,0,.2);text-align:center;line-height:1.3}
.btn-sample{background:var(--orange)}
.btn-buy{background:var(--red)}
.divider{height:32px;background:var(--brown)}

/* worries */
.worries{position:relative;height:400px;background:var(--beige)}
.worries-title{position:absolute;left:300px;top:20px;width:600px;height:90px;background:var(--white);border-radius:45px;box-shadow:0 4px 10px rgba(0,0,0,.12);display:flex;align-items:center;justify-content:center;font-size:42px;font-weight:900;color:var(--brown-dark)}
.worries-people{position:absolute;right:40px;top:130px;width:290px;height:230px;border-radius:12px;background:linear-gradient(160deg,#f5efe2,#e2d5bb)}
.worries-list{position:absolute;left:70px;top:130px;width:770px;list-style:none;background:var(--white);border-radius:10px;padding:12px 24px}
.worries-list li{display:flex;align-items:center;gap:12px;font-size:18px;font-weight:500;padding:5px 0;border-bottom:1px dashed #d8c9ad;white-space:nowrap}
.worries-list li svg{flex-shrink:0}
.worries-list li:last-child{border-bottom:none}
.worries-list em{font-style:normal;color:var(--red);font-weight:700}

/* good news */
.news{position:relative;height:260px;background:linear-gradient(180deg,var(--sky) 0%,#eef6fb 70%,var(--white) 100%);text-align:center;padding-top:46px}
.news .line1{font-size:44px;font-weight:900;color:var(--brown-dark)}
.news .line2{font-size:48px;font-weight:900;color:var(--brown-dark)}
.news .line2 em{font-style:normal;color:var(--orange)}
.news .line2 i{font-style:normal;color:var(--green)}

/* reasons */
.reasons{background:linear-gradient(180deg,var(--white),var(--cream));padding:20px 0 40px}
.reasons-title{margin:0 auto;width:1000px;height:90px;background:var(--brown);color:var(--white);display:flex;align-items:center;justify-content:center;gap:14px;font-size:38px;font-weight:900}
.reasons-title em{font-style:normal;font-size:56px;color:var(--gold)}
.reason{position:relative;margin:24px auto 0;width:1000px;height:190px;background:var(--white);border-top:4px solid var(--gold);display:flex;align-items:center;gap:30px;padding:0 30px;box-shadow:0 2px 8px rgba(0,0,0,.06)}
.reason.rev{flex-direction:row-reverse}
.reason-text{flex:1;position:relative;z-index:1}
.reason h3{font-size:28px;font-weight:900;color:var(--brown-dark);line-height:1.35}
.reason h3 em{font-style:normal;color:var(--orange)}
.reason p{font-size:15px;margin-top:8px;color:#5a4a3a}
.reason-photo{width:320px;height:150px;border-radius:6px;flex-shrink:0}
.reason-num{position:absolute;right:360px;bottom:-10px;font-size:120px;font-weight:900;color:rgba(91,58,29,.08);line-height:1}
.reason.rev .reason-num{right:auto;left:360px}

/* chosen */
.chosen{height:260px;display:flex;align-items:center;justify-content:center;gap:50px;background:var(--cream)}
.chosen-pack{width:280px;height:200px;border-radius:8px;background:linear-gradient(160deg,#c58a4a,#7b4a22)}
.chosen-copy{font-size:44px;font-weight:900;color:var(--brown-dark);line-height:1.4;text-align:center}
.chosen-copy em{font-style:normal;color:var(--orange)}
.chosen-cup{width:220px;height:180px;border-radius:50%;background:radial-gradient(#e0a95c,#f6ead2)}

/* column */
.column{position:relative;height:460px;background:linear-gradient(180deg,#e4f1f8,#f6fbfd)}
.column-card{position:absolute;left:200px;top:30px;width:800px;height:400px;background:var(--white);border-radius:14px;box-shadow:0 4px 14px rgba(0,0,0,.1);overflow:hidden}
.column-head{padding:24px 40px 10px;border-bottom:2px solid var(--sky)}
.column-label{font-size:16px;font-style:italic;color:#3b8fd0;font-weight:700}
.column-head h2{font-size:34px;font-weight:900;color:var(--brown-dark)}
.column-body{display:flex;gap:24px;padding:20px 40px}
.column-body p{flex:1;font-size:15px;line-height:1.9}
.column-body p em{font-style:normal;color:var(--red);font-weight:700}
.column-photo{width:260px;height:250px;border-radius:8px;background:linear-gradient(160deg,#eef3f6,#cfdbe2)}

/* voices */
.voices{position:relative;height:1296px;overflow:hidden}
.voices-bg{position:absolute;inset:0;background:var(--wood)}
.voices-board{position:absolute;left:190px;top:60px;width:820px;height:200px;background:var(--white);border-radius:10px;box-shadow:0 4px 10px rgba(0,0,0,.18);display:flex;flex-direction:column;align-items:center;justify-content:center;font-size:44px;font-weight:900;color:var(--brown-dark);line-height:1.35}
.voices-board em{font-style:normal;color:var(--orange);font-size:52px}
.bubble{position:absolute;width:150px;height:150px;border-radius:50%;background:var(--white);border:3px solid var(--green-light);display:flex;align-items:center;justify-content:center;text-align:center;font-size:17px;font-weight:700;color:var(--green);line-height:1.35}
.voice-list{position:absolute;left:60px;top:330px;width:1080px;display:flex;gap:30px}
.voice{flex:1;background:var(--white);border-radius:6px;padding:26px 22px;box-shadow:0 4px 10px rgba(0,0,0,.2);position:relative}
.voice::before{content:"";position:absolute;top:-10px;left:50%;width:20px;height:20px;margin-left:-10px;border-radius:50%;background:var(--red)}
.voice h3{font-size:28px;font-weight:900;color:var(--brown-dark);line-height:1.35}
.voice .who{font-size:14px;color:var(--brown-soft);margin:10px 0}
.voice p{font-size:15px;line-height:1.9}
.voice-photo{margin-top:20px;height:260px;border-radius:6px;background:linear-gradient(160deg,#f2ece0,#d9ccb4)}
</style>
</head>
<body>

<header class="site-header">
  <div class="brand"><span class="brand-dot"></span>あゆみ麦茶</div>
  <div class="tel">
    <span class="tel-tag">通話無料</span>
    <span class="tel-num">
      <svg width="26" height="26" viewBox="0 0 24 24"><path fill="#5b3a1d" d="M6.6 10.8a15.1 15.1 0 0 0 6.6 6.6l2.2-2.2c.3-.3.7-.4 1-.2 1.1.4 2.3.6 3.6.6.6 0 1 .4 1 1V20c0 .6-.4 1-1 1A17 17 0 0 1 3 4c0-.6.4-1 1-1h3.5c.6 0 1 .4 1 1 0 1.3.2 2.5.6 3.6.1.3 0 .7-.2 1z"/></svg>
      0120-456-789
    </span>
  </div>
</header>

<section class="hero">
  <div class="hero-bg" role="img" aria-label="公園の並木道の写真"></div>
  <div class="hero-people ph" role="img" aria-label="ウォーキングを楽しむシニア夫婦の写真"></div>
  <div class="hero-copy">
    <p class="sub">ウォーキングや日常での</p>
    <p class="main"><em>理想的な</em>水分補給を応援！</p>
  </div>
  <div class="pack ph" role="img" aria-label="あゆみ麦茶の商品パッケージ写真"></div>
  <p class="pack-spec">1箱4g×30包入り（日本製）</p>
  <p class="pack-note">7つの厳選素材・アミノ酸配合</p>
  <div class="badge badge-hot">ホット<br>でも！</div>
  <div class="badge badge-ice">アイス<br>でも！</div>
  <div class="feature-tags">
    <span>カロリー<br>ゼロ</span>
    <span>ノン<br>カフェイン</span>
    <span>糖質<br>ゼロ</span>
  </div>
  <div class="badge badge-price"><span>1Lあたり</span><b>33円</b></div>
  <p class="award">国際品質アワード金賞受賞スタッフが開発！</p>
</section>

<div class="guarantee">30日間・安心安全保証！ご納得いただけなければ<em>全額返金</em></div>

<section class="sample">
  <p class="sample-head"><em>今だけ限定！</em> 健康習慣のチャンス！</p>
  <div class="sample-row">
    <div class="sample-offer">無料1リットル分の無料サンプル<br>プレゼント実施中！</div>
    <div class="btn btn-sample">無料サンプル<br>はこちら</div>
    <div class="btn btn-buy">ご購入はこちら
      <svg width="18" height="18" viewBox="0 0 10 10"><path d="M3 1l4 4-4 4" stroke="#fff" stroke-width="2" fill="none"/></svg>
    </div>
  </div>
</section>
<div class="divider"></div>

<section class="worries">
  <h2 class="worries-title">こんなお悩みありませんか？</h2>
  <div class="worries-people ph" role="img" aria-label="悩むシニア夫婦のイラスト"></div>
  <ul class="worries-list">
    <li><svg width="22" height="22" viewBox="0 0 20 20"><rect x="1" y="1" width="18" height="18" fill="none" stroke="#5b3a1d" stroke-width="2"/><path d="M4 10l4 4 8-9" stroke="#d6392b" stroke-width="3" fill="none"/></svg><span>最近、<em>運動不足気味</em>かも…</span></li>
    <li><svg width="22" height="22" viewBox="0 0 20 20"><rect x="1" y="1" width="18" height="18" fill="none" stroke="#5b3a1d" stroke-width="2"/><path d="M4 10l4 4 8-9" stroke="#d6392b" stroke-width="3" fill="none"/></svg><span>ウォーキングの時って<em>何を飲めばいい</em>のだろう？</span></li>
    <li><svg width="22" height="22" viewBox="0 0 20 20"><rect x="1" y="1" width="18" height="18" fill="none" stroke="#5b3a1d" stroke-width="2"/><path d="M4 10l4 4 8-9" stroke="#d6392b" stroke-width="3" fill="none"/></svg><span>この先もずっと<em>アクティブでいたい！</em></span></li>
    <li><svg width="22" height="22" viewBox="0 0 20 20"><rect x="1" y="1" width="18" height="18" fill="none" stroke="#5b3a1d" stroke-width="2"/><path d="M4 10l4 4 8-9" stroke="#d6392b" stroke-width="3" fill="none"/></svg><span>運動時も日常も飲めるカラダに優しい<em>健康的な飲み物</em>が欲しい！</span></li>
    <li><svg width="22" height="22" viewBox="0 0 20 20"><rect x="1" y="1" width="18" height="18" fill="none" stroke="#5b3a1d" stroke-width="2"/><path d="M4 10l4 4 8-9" stroke="#d6392b" stroke-width="3" fill="none"/></svg><span>簡単なのに美味しく続けられる<em>「ラクラク健康習慣」</em>を手に入れたい！</span></li>
  </ul>
</section>

<section class="news serif">
  <p class="line1">＼ そんなあなたに朗報！ ／</p>
  <p class="line2"><i>あゆみ麦茶</i>で変わる<em>「カラダ健康生活」</em>！</p>
</section>

<section class="reasons">
  <h2 class="reasons-title serif">あゆみ麦茶が選ばれる<em>5</em>つの理由！</h2>

  <article class="reason">
    <div class="reason-text">
      <h3>7つの厳選成分を<em>「運動する大人」</em>の<br>ために贅沢ブレンド！</h3>
      <p>麦茶をベースに大麦・黒豆・はと麦など7つの穀物素材を独自に焙煎。香ばしさと栄養をまるごと閉じ込めました。</p>
    </div>
    <div class="reason-photo ph" role="img" aria-label="穀物素材の写真" style="background:linear-gradient(160deg,#e8d9bb,#b79668)"></div>
    <span class="reason-num">1</span>
  </article>

  <article class="reason rev">
    <div class="reason-text">
      <h3>運動時や日常生活で大切な<br><em>必須アミノ酸、チロシン</em>を配合！</h3>
      <p>体づくりを支えるアミノ酸を手軽に補給。毎日の散歩や家事の合間にもおすすめです。</p>
    </div>
    <div class="reason-photo ph" role="img" aria-label="笑顔で歩くシニアの写真" style="background:linear-gradient(160deg,#f1ece0,#d7e3c3)"></div>
    <span class="reason-num">2</span>
  </article>

  <article class="reason">
    <div class="reason-text">
      <h3>嬉しい、<em>糖質＆脂質ゼロ</em><br>＆ノンカフェイン！</h3>
      <p>カロリーを気にせず、夜や寝る前にも安心して飲めます。ご家族みんなで楽しめます。</p>
    </div>
    <div class="reason-photo ph" role="img" aria-label="家族で過ごすシニアの写真" style="background:linear-gradient(160deg,#f3eee3,#dcd2bd)"></div>
    <span class="reason-num">3</span>
  </article>

  <article class="reason rev">
    <div class="reason-text">
      <h3>どんな食事とも合う、香ばしく<br><em>豊かな味わい！</em></h3>
      <p>和食にも洋食にもぴったり。ホットでもアイスでも、季節を問わずおいしく飲めます。</p>
    </div>
    <div class="reason-photo ph" role="img" aria-label="和食の食卓の写真" style="background:linear-gradient(160deg,#efe3d0,#caa77b)"></div>
    <span class="reason-num">4</span>
  </article>

  <article class="reason">
    <div class="reason-text">
      <h3>確かな<em>品質管理体制</em><br>（放射能検査・残留農薬検査も実施）</h3>
      <p>国内工場で厳しい検査を行い、安心してお飲みいただける品質をお届けしています。</p>
    </div>
    <div class="reason-photo ph" role="img" aria-label="品質検査の様子の写真" style="background:linear-gradient(160deg,#eef2f4,#c9d4da)"></div>
    <span class="reason-num">5</span>
  </article>
</section>

<section class="chosen">
  <div class="chosen-pack ph" role="img" aria-label="あゆみ麦茶の商品パッケージ写真"></div>
  <p class="chosen-copy serif">だから<br><em>あゆみ麦茶</em>は<br>多くの方に選ばれています</p>
  <div class="chosen-cup ph" role="img" aria-label="麦茶の入ったティーカップの写真"></div>
</section>

<section class="column">
  <div class="column-card">
    <div class="column-head">
      <p class="column-label">Column</p>
      <h2>水分補給の大切さとあゆみ麦茶</h2>
    </div>
    <div class="column-body">
      <p>体の約60％は水分でできています。それだけ体にとって水分は大切な存在です。<em>歩く前後のこまめな水分補給</em>が健康づくりの基本です。<br>のどが渇いたと感じる前に、少しずつ飲むことを心がけましょう。あゆみ麦茶はミネラルを含み、カフェインゼロなので<em>毎日の習慣</em>にぴったり。ご家族の健康づくりにもお役立てください。</p>
      <div class="column-photo ph" role="img" aria-label="水を手にした女性の写真"></div>
    </div>
  </div>
</section>

<section class="voices">
  <div class="voices-bg" role="img" aria-label="木目の板の背景"></div>
  <div class="voices-board serif">全国からご利用者さまの声が、<em>ぞくぞく届いています！</em></div>
  <div class="bubble" style="left:40px;top:120px">ウォーキング<br>がもっと楽しく<br>なりました！</div>
  <div class="bubble" style="right:40px;top:90px">家族みんなで<br>飲んで<br>います！</div>
  <div class="voice-list">
    <article class="voice">
      <h3>心も体も健康に、夫婦で毎日飲んでいます</h3>
      <p class="who">北海道・70代 女性</p>
      <p>毎朝夫婦で散歩するのが日課です。香ばしくて飲みやすく、水筒に入れて持ち歩いています。体の調子も良く、続けて良かったと感じています。</p>
      <div class="voice-photo ph" role="img" aria-label="散歩するシニア夫婦の写真"></div>
    </article>
    <article class="voice">
      <h3>心も体も健康に、夫婦で毎日飲んでいます</h3>
      <p class="who">東京都・60代 男性</p>
      <p>カフェインがないので夜も安心して飲めます。食事にもよく合い、家族にも好評です。これからも毎日の習慣にしていきたいと思います。</p>
      <div class="voice-photo ph" role="img" aria-label="お茶を楽しむシニア夫婦の写真"></div>
    </article>
    <article class="voice">
      <h3>心も体も健康に、夫婦で毎日飲んでいます</h3>
      <p class="who">大阪府・70代 女性</p>
      <p>ホットでもアイスでもおいしいので一年中飲んでいます。ウォーキング仲間にもすすめたら、みんな気に入ってくれました。</p>
      <div class="voice-photo ph" role="img" aria-label="笑顔のシニア夫婦の写真"></div>
    </article>
  </div>
</section>

</body>
</html>
```